High Tech Real Estate Startup needs a business card

We are developing an innovative real estate marketing product based around advanced search and virtual reality.

We talk to people, we need business cards.

Target Market(s)

The target market is technology professionals and realtors.

Contact Information for Business Card

The information to be included will include

Name
Title
Phone Number
E-mail Address
www.quelzo.com

It should use simple iconography for each one of those fields.

Font styles to use
Other font styles liked:
• Co, Jubilat, Avenir

Colors

Designer to choose colors to be used in the design.

Requirements
Must have
• Clean aesthetic,
• Good use of negative space.
• It should use our company logo, shown in the attached file. It is able to use the negative of that logo (coloured font and white background) and I have attached other acceptable accent colours in a swatch file.
Should not have
• Should not be too busy
• No extraneous text (slogans, tag lines etc)

```html
<!DOCTYPE html>
<html lang="en">
<head>
<meta charset="utf-8">
<title>Quelzo Business Card</title>
<link rel="stylesheet" href="https://fonts.googleapis.com/css2?family=Roboto+Slab:wght@700;800&family=Montserrat:wght@500&display=swap">
<style>
  :root {
    --backdrop: #9d9e9e;
    --charcoal: #2b2b2b;
    --sky: #009fe0;
    --paper: #ffffff;
  }
  * { margin: 0; padding: 0; box-sizing: border-box; }
  html, body {
    width: 1183px; height: 1200px; overflow: hidden;
    background: var(--backdrop);
  }
  .sheet {
    position: absolute; left: 0; top: 0;
    width: 1416px; height: 1436px;
    transform: scale(0.83545); transform-origin: 0 0;
  }
  .card { position: absolute; background: var(--paper); overflow: hidden; }
  .card-front { left: 155px; top: 60px; width: 1126px; height: 638px; }
  .card-back { left: 135px; top: 738px; width: 1110px; height: 637px; }
  .card-shapes { position: absolute; inset: 0; width: 100%; height: 100%; }

  .slab { font-family: "Roboto Slab", Georgia, serif; font-weight: 800; }

  .icon {
    position: absolute; left: 35px; width: 56px; height: 56px;
    border-radius: 50%; background: var(--paper);
  }
  .icon svg { width: 56px; height: 56px; display: block; }

  .person-name {
    position: absolute; left: 134px; top: 122px;
    color: var(--paper); font-size: 44px; line-height: 1; letter-spacing: -1px;
  }
  .person-title {
    position: absolute; left: 134px; top: 172px;
    color: var(--charcoal); font-size: 40px; line-height: 1;
  }
  .contact-line {
    position: absolute; left: 134px;
    color: var(--paper); font-size: 38px; line-height: 1; font-weight: 700;
  }
  .rule {
    position: absolute; left: 134px; width: 331px; height: 3px;
    background: var(--paper);
  }

  .brand-box {
    position: absolute; background: var(--sky); color: var(--paper);
    display: flex; align-items: center; justify-content: center;
    font-family: "Montserrat", Arial, sans-serif; font-weight: 500;
  }
  .brand-box-front {
    left: 723px; top: 237px; width: 293px; height: 123px;
    font-size: 56px; letter-spacing: 1px;
  }
  .brand-frame {
    position: absolute; left: 269px; top: 196px; width: 300px; height: 244px;
    border: 3px solid var(--paper); border-right: none;
  }
  .brand-box-back {
    left: 275px; top: 202px; width: 559px; height: 232px;
    font-size: 82px; letter-spacing: 2px;
  }
</style>
</head>
<body>
<div class="sheet">

  <section class="card card-front">
    <svg class="card-shapes" viewBox="0 0 1126 638" aria-hidden="true">
      <polygon fill="var(--charcoal)" points="0,0 403,0 455,110 0,110"/>
      <polygon fill="var(--sky)" points="403,0 455,0 507,110 455,110"/>
      <polygon fill="var(--sky)" points="0,110 457,110 513,228 0,228"/>
      <polygon fill="var(--charcoal)" points="0,228 513,228 717,638 0,638"/>
      <polygon fill="var(--sky)" points="513,228 563,228 767,638 717,638"/>
      <polygon fill="var(--sky)" points="543,178 547,178 565,228 561,228"/>
    </svg>

    <div class="icon" style="top:137px">
      <svg viewBox="0 0 56 56"><circle cx="28" cy="21" r="7" fill="var(--charcoal)"/><path d="M15 40c0-8 6-11 13-11s13 3 13 11z" fill="var(--charcoal)"/></svg>
    </div>
    <div class="person-name slab">NAME</div>
    <div class="person-title slab">Title</div>

    <div class="icon" style="top:333px">
      <svg viewBox="0 0 56 56"><path d="M20 14c2-1 4 0 5 2l2 5c0 2-1 3-3 4 1 4 3 7 6 9 1-2 3-3 4-2l5 3c2 1 2 3 1 5-2 2-5 3-8 2-8-3-14-10-16-19 0-4 1-7 4-9z" fill="none" stroke="var(--charcoal)" stroke-width="3"/></svg>
    </div>
    <div class="contact-line slab" style="top:342px">Phone Number</div>
    <div class="rule" style="top:405px"></div>

    <div class="icon" style="top:424px">
      <svg viewBox="0 0 56 56"><rect x="12" y="17" width="32" height="22" fill="none" stroke="var(--charcoal)" stroke-width="2.5"/><path d="M12 17l16 13 16-13M12 39l12-11M44 39l-12-11" fill="none" stroke="var(--charcoal)" stroke-width="2"/></svg>
    </div>
    <div class="contact-line slab" style="top:432px">E-mail Address</div>
    <div class="rule" style="top:495px"></div>

    <div class="icon" style="top:505px">
      <svg viewBox="0 0 56 56"><g fill="none" stroke="var(--charcoal)" stroke-width="2"><circle cx="28" cy="28" r="16"/><ellipse cx="28" cy="28" rx="7" ry="16"/><path d="M12 28h32M14 20h28M14 36h28M28 12v32"/></g></svg>
    </div>
    <div class="contact-line slab" style="top:513px">www.quelzo.com</div>

    <div class="brand-box brand-box-front">QUELZO</div>
  </section>

  <section class="card card-back">
    <svg class="card-shapes" viewBox="0 0 1110 637" aria-hidden="true">
      <rect x="0" y="0" width="555" height="637" fill="var(--charcoal)"/>
    </svg>
    <div class="brand-frame"></div>
    <div class="brand-box brand-box-back">QUELZO</div>
  </section>

</div>
</body>
</html>
```